Property Management Company Business Cards

Need business cards for a property management company located in Michigan. We manage houses for clients all over the world. Young and modern company, looking for eye catching design. Please work with the attached logo.

Industry/Entity Type

Property Management

Requirements
Must have
• Need lines for address, telephone number, fax number, web site.

Also lines for name, and job title

```html
<!DOCTYPE html>
<html lang="en">
<head>
<meta charset="utf-8">
<title>Lakeshore Crest Management – Stationery</title>
<link rel="stylesheet" href="https://fonts.googleapis.com/css2?family=Open+Sans:wght@400;600;700&display=swap">
<style>
  :root {
    --sky: #22a8e0;
    --sky-light: #2ec3ee;
    --charcoal: #363638;
    --paper: #ffffff;
    --paper-shade: #ececec;
    --stage: #d9d9d9;
    --ink: #2c2c2e;
  }
  * { box-sizing: border-box; margin: 0; padding: 0; }
  html, body {
    width: 1200px; height: 861px; overflow: hidden;
    background: var(--stage);
    font-family: "Open Sans", Arial, sans-serif;
  }
  .stage { position: relative; width: 1200px; height: 861px; }

  /* Folder spread */
  .folder {
    position: absolute; left: 70px; top: 70px;
    width: 700px; height: 480px;
    display: flex;
    box-shadow: 0 12px 30px rgba(0,0,0,.25);
  }
  .folder-back {
    position: relative; width: 350px; height: 100%;
    background: linear-gradient(120deg, var(--sky-light), var(--sky));
    color: var(--paper);
  }
  .folder-back .pocket-edge {
    position: absolute; right: 0; top: 0; width: 1px; height: 100%;
    background: rgba(0,0,0,.15);
  }
  .folder-back .brand { position: absolute; left: 22px; bottom: 64px; }
  .folder-back .brand-name { font-size: 10px; }
  .folder-back .contact {
    position: absolute; left: 22px; bottom: 22px;
    font-size: 6.5px; line-height: 1.5; font-weight: 600;
  }
  .folder-front {
    position: relative; width: 350px; height: 100%;
    background: linear-gradient(90deg, var(--paper) 55%, var(--paper-shade));
  }
  .folder-front svg { position: absolute; inset: 0; }
  .folder-front .brand { position: absolute; left: 172px; top: 196px; }
  .folder-front .brand-name { font-size: 13px; }
  .folder-front .brand-dot { width: 20px; height: 20px; }

  /* Wordmark stand-in */
  .brand { display: flex; align-items: center; gap: 7px; }
  .brand-dot { width: 14px; height: 14px; border-radius: 50%; background: currentColor; flex: none; }
  .brand-name { font-weight: 700; letter-spacing: .3px; line-height: 1.15; white-space: nowrap; }
  .brand-name span { display: block; }
  .on-dark { color: var(--paper); }
  .on-light { color: var(--ink); }

  /* Business card */
  .card {
    position: absolute; left: 790px; top: 590px;
    width: 360px; height: 206px;
    background: linear-gradient(90deg, var(--paper) 60%, var(--paper-shade));
    box-shadow: 0 10px 24px rgba(0,0,0,.25);
  }
  .card svg { position: absolute; inset: 0; }
  .card .holder { position: absolute; left: 16px; top: 18px; color: var(--paper); }
  .holder-name { font-size: 15px; font-weight: 600; }
  .holder-title { font-size: 9px; opacity: .9; }
  .card .details {
    position: absolute; left: 16px; top: 92px; list-style: none;
    color: var(--paper); font-size: 7.5px; line-height: 1.4;
  }
  .details li { display: flex; gap: 5px; margin-bottom: 5px; }
  .details svg { position: static; width: 8px; height: 8px; flex: none; margin-top: 1px; }
  .card .brand { position: absolute; left: 186px; top: 88px; }
  .card .brand-name { font-size: 10px; }
</style>
</head>
<body>
<main class="stage">

  <section class="folder" aria-label="Presentation folder">
    <div class="folder-back">
      <span class="pocket-edge"></span>
      <div class="brand on-dark">
        <span class="brand-dot"></span>
        <span class="brand-name">LAKESHORE CREST MANAGEMENT</span>
      </div>
      <p class="contact">
        15th Floor, Lorem Ipsum Avenue, Dolor Sit Amet City<br>
        Telephone: 123.456.7890 • Fax: 123.456.7890<br>
        E-mail: name@lcmanagement.com • Web: www.lcmanagement.com
      </p>
    </div>
    <div class="folder-front">
      <svg width="350" height="480" viewBox="0 0 350 480" aria-hidden="true">
        <polygon points="0,0 20,0 128,220 128,480 0,480" fill="var(--sky)"/>
        <polygon points="30,0 52,0 154,210 154,480 134,480 134,224" fill="var(--charcoal)"/>
      </svg>
      <div class="brand on-light">
        <span class="brand-dot"></span>
        <span class="brand-name"><span>LAKESHORE CREST</span><span>MANAGEMENT</span></span>
      </div>
    </div>
  </section>

  <section class="card" aria-label="Business card">
    <svg width="360" height="206" viewBox="0 0 360 206" aria-hidden="true">
      <polygon points="0,0 138,0 156,103 138,206 0,206" fill="var(--sky)"/>
      <polygon points="138,0 150,0 168,103 150,206 138,206 156,103" fill="var(--charcoal)"/>
    </svg>
    <div class="holder">
      <p class="holder-name">Name Surname</p>
      <p class="holder-title">Your Position</p>
    </div>
    <ul class="details">
      <li>
        <svg viewBox="0 0 10 10"><path d="M5 1 L9.5 5 H8 V9 H6 V6.5 H4 V9 H2 V5 H0.5 Z" fill="#fff"/></svg>
        <span>15th floor, Lorem Ipsum Avenue,<br>Dolor Sit Amet City</span>
      </li>
      <li>
        <svg viewBox="0 0 10 10"><path d="M2 1 L4 1 L4.5 3.5 L3.3 4.3 Q4.5 6.5 5.7 6.7 L6.5 5.5 L9 6 L9 8 Q6 9.5 3 6.5 Q0.5 4 2 1 Z" fill="#fff"/></svg>
        <span>123.456.7890</span>
      </li>
      <li>
        <svg viewBox="0 0 10 10"><rect x="2.5" y="1" width="5" height="3" fill="#fff"/><rect x="1" y="4" width="8" height="4" rx="1" fill="#fff"/></svg>
        <span>098.765.4321</span>
      </li>
      <li>
        <svg viewBox="0 0 10 10"><rect x="1" y="1.5" width="8" height="7" fill="none" stroke="#fff" stroke-width="1.2"/><rect x="1" y="1.5" width="8" height="2" fill="#fff"/></svg>
        <span>www.lcmanagement.com</span>
      </li>
    </ul>
    <div class="brand on-light">
      <span class="brand-dot"></span>
      <span class="brand-name"><span>LAKESHORE CREST</span><span>MANAGEMENT</span></span>
    </div>
  </section>

</main>
</body>
</html>
```